Industrial / automotive service company
Renewing and reconditioning solutions
Simple
Ted Pelkin
VP - Industrial Division
217 Marston Crescent NW
Calgary, Alberta
T2P 4G6
t-pelkin@zorvamail.com

```html
<!DOCTYPE html>
<html lang="en">
<head>
<meta charset="utf-8">
<title>Tovalmex Services Inc. – Business Cards</title>
<link rel="stylesheet" href="https://fonts.googleapis.com/css2?family=Montserrat:wght@400;500;600;800&display=swap">
<style>
  :root {
    --bg-top: #e4e5e7;
    --bg-bottom: #c9cacc;
    --card: #ffffff;
    --green: #8cc63f;
    --green-dark: #6fa82a;
    --grey: #a7a9ac;
    --grey-light: #d1d3d4;
    --text: #6d6e71;
  }
  * { margin: 0; padding: 0; box-sizing: border-box; }
  html, body { width: 1200px; height: 987px; overflow: hidden; }
  body {
    background: linear-gradient(180deg, var(--bg-top), var(--bg-bottom));
    font-family: "Montserrat", Arial, sans-serif;
    position: relative;
  }
  .card {
    position: absolute;
    left: 230px;
    width: 740px;
    height: 423px;
    background: var(--card);
    border-radius: 22px;
    overflow: hidden;
    box-shadow: 0 10px 28px rgba(0,0,0,0.18);
  }
  .card--front { top: 52px; }
  .card--back { top: 512px; }

  .brand {
    position: absolute;
    display: flex;
    align-items: center;
    gap: 16px;
  }
  .brand__mark {
    width: 54px; height: 54px;
    border-radius: 50%;
    background: var(--green);
    flex: none;
  }
  .brand__name {
    color: var(--green);
    font-weight: 800;
    line-height: 1;
    letter-spacing: 1px;
    text-transform: uppercase;
  }
  .brand__name span { display: block; font-size: 0.42em; letter-spacing: 4px; margin-top: 6px; }

  .card--front .brand { left: 200px; top: 140px; }
  .card--front .brand__name { font-size: 52px; }
  .website {
    position: absolute;
    left: 200px; top: 268px;
    color: var(--green);
    font-size: 17px;
    font-weight: 500;
    letter-spacing: 5px;
    font-variant: small-caps;
  }

  .card--back .brand { left: 220px; top: 36px; }
  .card--back .brand__mark { width: 44px; height: 44px; }
  .card--back .brand__name { font-size: 42px; }

  .person {
    position: absolute;
    left: 370px; top: 150px;
    text-align: center;
    transform: translateX(-50%);
    font-variant: small-caps;
  }
  .person__name { color: var(--green); font-size: 18px; font-weight: 600; letter-spacing: 2px; }
  .person__role { color: var(--text); font-size: 13px; letter-spacing: 2px; margin-top: 4px; }

  .contact {
    position: absolute;
    top: 208px;
    font-size: 12.5px;
    color: var(--text);
    letter-spacing: 1.5px;
    line-height: 21px;
    font-variant: small-caps;
  }
  .contact--address { right: 385px; text-align: right; }
  .contact--reach { left: 385px; }
  .contact__divider {
    position: absolute;
    left: 369px; top: 210px;
    width: 2px; height: 82px;
    background: var(--green);
  }
  .contact--reach li { list-style: none; display: flex; align-items: center; gap: 8px; }
  .contact--reach svg { width: 14px; height: 14px; flex: none; }
  .swoosh { position: absolute; left: 0; bottom: 0; width: 740px; height: 423px; }
</style>
</head>
<body>
  <section class="card card--front">
    <div class="brand">
      <div class="brand__mark"></div>
      <div class="brand__name">Tovalmex<span>Services Inc.</span></div>
    </div>
    <p class="website">www.tovalmexservices.com</p>
  </section>

  <section class="card card--back">
    <svg class="swoosh" viewBox="0 0 740 423" aria-hidden="true">
      <path d="M0 292 C 140 340, 330 372, 740 358 L740 423 L0 423 Z" fill="var(--grey-light)"/>
      <path d="M0 318 C 150 372, 360 396, 740 376 L740 423 L0 423 Z" fill="var(--grey)"/>
      <path d="M0 340 C 160 400, 380 412, 740 396 L740 423 L0 423 Z" fill="var(--green)"/>
    </svg>
    <div class="brand">
      <div class="brand__mark"></div>
      <div class="brand__name">Tovalmex<span>Services Inc.</span></div>
    </div>
    <div class="person">
      <p class="person__name">Ted Pelkin</p>
      <p class="person__role">VP - Industrial Division</p>
    </div>
    <address class="contact contact--address" style="font-style:normal">
      217 Marston Crescent NW<br>
      Calgary, Alberta<br>
      T2P 4G6
    </address>
    <div class="contact__divider"></div>
    <ul class="contact contact--reach">
      <li>
        <svg viewBox="0 0 14 14" aria-hidden="true"><circle cx="7" cy="7" r="7" fill="var(--green)"/><path d="M4.5 3.5 L6 5 L5.2 6 C5.7 7.2 6.8 8.3 8 8.8 L9 8 L10.5 9.5 L9.5 10.6 C6.8 10.3 3.7 7.2 3.4 4.5 Z" fill="#fff"/></svg>
        (403) 555-0147
      </li>
      <li>
        <svg viewBox="0 0 14 14" aria-hidden="true"><circle cx="7" cy="7" r="7" fill="var(--green)"/><rect x="3.5" y="4.5" width="7" height="5" fill="none" stroke="#fff" stroke-width="1"/><path d="M3.5 4.5 L7 7.3 L10.5 4.5" fill="none" stroke="#fff" stroke-width="1"/></svg>
        t-pelkin@zorvamail.com
      </li>
      <li>
        <svg viewBox="0 0 14 14" aria-hidden="true"><circle cx="7" cy="7" r="7" fill="var(--green)"/><circle cx="7" cy="7" r="3.6" fill="none" stroke="#fff" stroke-width="1"/><path d="M3.4 7 H10.6 M7 3.4 C5.5 5 5.5 9 7 10.6 M7 3.4 C8.5 5 8.5 9 7 10.6" fill="none" stroke="#fff" stroke-width="0.8"/></svg>
        www.tovalmexservices.com
      </li>
    </ul>
  </section>
</body>
</html>
```